Non profit organization looking for new flyers as "leaflets"

Hi, we are looking for new flyers in form "leaflets in German :-)" i've attached our old flyer, we have new logo and thats why we need new and better design smt ... "New: I've so attached the text Regarding the old cards with minor changes "

Industry/Entity Type

Non Profit

Font styles to use
Sans Serif

```html
<!DOCTYPE html>
<html lang="de">
<head>
<meta charset="utf-8">
<title>Ambulante Erziehungshilfe – Faltblatt</title>
<link rel="stylesheet" href="https://fonts.googleapis.com/css2?family=Libre+Baskerville:wght@700&family=Open+Sans:wght@400;600;700&display=swap">
<style>
:root{
  --blue:#1e8fd6;
  --blue-dark:#1a5d9f;
  --blue-panel:#4a86bf;
  --blue-pale:#dce9f4;
  --ink:#2b2b2b;
  --paper:#f7f8fa;
  --grey-bg:#e9ebee;
  --green:#8cbf2a;
}
*{box-sizing:border-box;margin:0;padding:0}
html,body{width:1200px;height:986px;overflow:hidden;background:var(--grey-bg)}
body{font-family:"Open Sans",Arial,sans-serif;color:var(--ink);position:relative}
.spread{position:absolute;left:50px;width:1100px;height:470px;display:flex;box-shadow:0 4px 14px rgba(0,0,0,.18);background:var(--paper)}
.spread--inside{top:16px}
.spread--outside{top:500px}
.panel{position:relative;width:366.66px;height:470px;overflow:hidden;border-right:1px solid #d9dde2}
.panel:last-child{border-right:none}
.heading{font-family:"Libre Baskerville",Georgia,serif;font-weight:700;text-transform:uppercase;color:#1d1d1d;letter-spacing:.3px}
.photo{position:absolute}
.deco{position:absolute;left:0;top:0}

/* inside panel 1 */
.motto{position:absolute;left:22px;top:250px;width:320px;font-size:12.5px;line-height:1.25}
.intro{position:absolute;left:22px;top:318px;width:320px;font-size:8.8px;line-height:1.35}
.law-list{position:absolute;left:22px;top:392px;width:320px;font-size:8.8px;line-height:1.35;list-style:none}
.law-list li{display:flex;align-items:baseline}
.law-list .label{white-space:nowrap}
.law-list .dots{flex:1;border-bottom:1px dotted #555;margin:0 3px;transform:translateY(-2px)}

/* inside panel 2 */
.offers{position:absolute;left:22px;top:300px;width:330px}
.offers .heading{font-size:14px;margin-bottom:8px}
.offers ul{list-style:none;font-size:9.6px;line-height:1.4}

/* inside panel 3 */
.goals{position:absolute;left:20px;top:16px;width:330px}
.goals .heading{font-size:14px;margin:0 0 4px}
.goals .heading + ul{margin-bottom:10px}
.goals ul{list-style:none;font-size:8.9px;line-height:1.28}

/* outside panel 1 */
.team-title{position:absolute;left:20px;top:220px;font-size:12px}
.team-text{position:absolute;left:20px;top:256px;width:240px;font-size:8.4px;line-height:1.4}
.brand-small{position:absolute;right:22px;bottom:18px;display:flex;align-items:center;gap:6px;font-weight:700;font-size:16px;color:var(--blue-dark)}
.brand-dot{width:12px;height:12px;background:var(--green);border-radius:50%}

/* outside panel 2 */
.panel--contact{background:var(--blue-panel);color:#fff}
.address{position:absolute;left:30px;width:300px;font-size:10px;line-height:1.35;padding-left:18px}
.address svg{position:absolute;left:0;top:1px}
.map{position:absolute;left:60px;top:300px;width:170px;height:100px;border-radius:30px 60px 20px 50px;background:#fff}
.badges{position:absolute;left:170px;bottom:14px;display:flex;gap:8px}
.badge{width:42px;height:42px;background:#fff;border-radius:4px}
.badge--round{border-radius:50%;background:#eef2f6}

/* outside panel 3 - cover */
.panel--cover{background:linear-gradient(180deg,#eef3f8 0%,#d6e5f2 100%)}
.cover-title{position:absolute;left:150px;top:30px;width:200px;text-align:center;font-size:15px;line-height:1.25}
.brand{position:absolute;left:40px;top:320px;display:flex;align-items:center;gap:8px;font-weight:700;font-size:30px;color:var(--blue-dark);letter-spacing:.5px}
.brand-mark{width:26px;height:26px;background:var(--green)}
.tagline{position:absolute;left:40px;top:362px;font-size:14px;line-height:1.25;color:#444}
.tagline .ar{font-size:16px;font-weight:600;direction:rtl;display:block;text-align:left}
</style>
</head>
<body>

<section class="spread spread--inside">
  <article class="panel panel--motto">
    <div class="photo" role="img" aria-label="Foto: lachende Familie mit zwei Kindern liest gemeinsam ein Buch auf dem Sofa"
         style="left:0;top:0;width:250px;height:232px;background:linear-gradient(135deg,#f1ede6,#d9c7b3 55%,#b9a590);clip-path:polygon(0 0,100% 0,100% 70%,78% 100%,0 100%)"></div>
    <svg class="deco" width="367" height="240" viewBox="0 0 367 240" aria-hidden="true">
      <polygon points="175,0 367,0 367,40 240,180" fill="#fff"/>
      <path d="M200 20 L290 20 Q300 20 296 30 L220 130 Z" fill="var(--blue)"/>
      <path d="M260 0 L367 0 L367 25 L300 120 Q290 135 280 120 Z" fill="#2e9ee3" opacity=".9"/>
      <path d="M196 205 Q200 190 214 192 L300 140 L300 170 Z" fill="var(--blue-dark)"/>
    </svg>
    <h2 class="heading motto">Wer ständig glücklich sein möchte muss sich oft verändern (Ludwig Hainer)</h2>
    <p class="intro">Den Weg zur Veränderung und zur Aufarbeitung von Erziehungsschwierigkeiten können sie mit Unterstützung unserer qualifizierten Fachkräfte finden. Wir werden dabei in Auftrag des Jugendamtes tätig und führen Hilfe nach § 27 ff des Kinder und Jugendhilfen-gesetzes durch:</p>
    <ul class="law-list">
      <li><span class="label">-Hilfe zur Erziehung</span><span class="dots"></span>§ 27</li>
      <li><span class="label">-Erziehungsberatung</span><span class="dots"></span>§ 28</li>
      <li><span class="label">-Erziehungsbeistands Schaft</span><span class="dots"></span>§ 30</li>
      <li><span class="label">-sozialpädagogische Familienhilfe</span><span class="dots"></span>§ 31</li>
      <li><span class="label">-Intensive sozialpädagogische Einzelbetreuung</span></li>
      <li><span class="label">(in Verbindung mit §41)</span><span class="dots"></span>§ 35</li>
    </ul>
  </article>

  <article class="panel panel--offers">
    <div class="photo" role="img" aria-label="Foto: Mann im Anzug streckt die Hand zum Gruß entgegen"
         style="left:60px;top:0;width:306px;height:280px;background:linear-gradient(160deg,#e3e6ea 0%,#6d7785 45%,#1f2630 100%)"></div>
    <svg class="deco" width="367" height="300" viewBox="0 0 367 300" aria-hidden="true">
      <polygon points="0,0 60,0 60,280 0,280" fill="#f3f4f6"/>
      <polygon points="0,70 90,0 140,0 0,110" fill="var(--blue)"/>
      <polygon points="0,110 140,0 160,0 0,125" fill="var(--blue-dark)"/>
    </svg>
    <div class="offers">
      <h2 class="heading">Unsere Angebote</h2>
      <ul>
        <li>-Hausbesuche/familienbesuche</li>
        <li>-Elternarbeit</li>
        <li>-Einzelgespräche/Klienten-zentrierte-Gespräche</li>
        <li>-Lösungsfokussierte arbeite</li>
        <li>-Sportliche Tätigkeit / Anbindung an vereinen und Gemeinwesen</li>
        <li>-Interkulturelle Arbeit</li>
        <li>-Anbindung an soziale Einrichtung</li>
        <li>-Kontakt zu Kindergarten und schulen /soziale Vernetzung im Stadtteil</li>
      </ul>
    </div>
  </article>

  <article class="panel panel--goals">
    <div class="goals">
      <h2 class="heading">Unsere Ziele</h2>
      <ul>
        <li>-Sicherung und Wiederherstellung der Erziehungsfunktion der Familie</li>
        <li>-Hilfe in verschiedenen Bereichen für Menschen mit ZUWANDERUNGSGESCHICHTE</li>
        <li>-Lösung- und ressourcenorientierte Arbeit</li>
        <li>-Verstärkung des Selbstwertgefühls der einzelnen Familienmitglieder</li>
        <li>-Verbesserung der Wahrnehmung von Erziehungsverantwortung</li>
        <li>-Konkrete Hilfestellung bei der Bewältigung von Alltagsproblemen</li>
        <li>-Erhöhung der Beziehungsfähigkeit der Kinder und Jugendlichen</li>
      </ul>
      <h2 class="heading">Unsere Zielgruppen</h2>
      <ul>
        <li>-Kinder und Jugendliche mit MIGRATIONHINTERFRUND</li>
        <li>-Kinder und Jugendliche die zwischen zwei Kulturen leben und daraus folgenden Belastungen</li>
        <li>-Erziehungsprobleme der MIGRATIONSKINDER</li>
        <li>-Bildungsprobleme der Jugendlichen mit MIGRATIONSHINTERGRUND</li>
        <li>-Schulverweigerer</li>
        <li>-Kinder und Jugendlichen mit Lernbehinderung</li>
        <li>-Kinder und Jugendlichen die im Verselbständigungsprozess Hilfe brauchen</li>
        <li>-Kinder und Jugendlichen mit Defiziten in der Persönlichkeitsentwicklung</li>
        <li>-Kinder und Jugendlichen mit erheblichen Beziehungsstörungen zu ihren Eltern</li>
        <li>-Familien mit MIGRATIONSINTERGRUND</li>
        <li>-Familien die keine bzw. schlechten INTEGRATIONSPROZESS DURCHFÜHREN</li>
        <li>-Familien die keine Anbindung an Kindern herstellen</li>
        <li>-Familien mit Problemen im Alltag und in der Erziehung</li>
      </ul>
    </div>
  </article>
</section>

<section class="spread spread--outside">
  <article class="panel panel--team">
    <div class="photo" role="img" aria-label="Foto: geöffnete Hände halten ein Netzwerk aus Personensymbolen vor dunklem Anzug"
         style="left:0;top:0;width:367px;height:228px;background:radial-gradient(circle at 45% 45%,#5b6d86 0%,#1e2a3d 60%,#111821 100%)"></div>
    <svg class="deco" width="367" height="470" viewBox="0 0 367 470" aria-hidden="true">
      <polygon points="0,190 290,215 290,245 0,245" fill="#fff"/>
      <polygon points="200,215 290,215 300,232" fill="var(--blue)"/>
      <polygon points="0,380 0,470 160,470" fill="var(--blue)"/>
      <polygon points="0,420 0,470 90,470" fill="var(--blue-dark)"/>
    </svg>
    <h2 class="heading team-title">Unser Team</h2>
    <p class="team-text">Unser Team besteht aus qualifizierten Fachkräften mit viel Erfahrung in Erziehungsproblemen. Durch die Herkunft unserer Fachkräfte aus verschiedenen Ländern können wir ihnen in 6 Sprachen behilflich sein. Darunter fallen: Deutsch, Türkisch, Arabisch, Französisch, kurdisch und Englisch</p>
    <div class="brand-small"><span class="brand-dot"></span>lumen</div>
  </article>

  <article class="panel panel--contact">
    <div class="address" style="top:40px">
      <svg width="11" height="14" viewBox="0 0 11 14" aria-hidden="true"><path d="M5.5 0A5.5 5.5 0 0 0 0 5.5C0 9.5 5.5 14 5.5 14S11 9.5 11 5.5A5.5 5.5 0 0 0 5.5 0Z" fill="#9ccc3a"/><circle cx="5.5" cy="5.5" r="2" fill="#fff"/></svg>
      Lumen Bildungsforum e.V<br>Lindenplatz 7 – 58210 Hellbach<br>Telefon : (0 21 10) 45 17 30<br>Telefax : (0 21 10) 45 17 31
    </div>
    <div class="address" style="top:125px">
      <svg width="11" height="14" viewBox="0 0 11 14" aria-hidden="true"><path d="M5.5 0A5.5 5.5 0 0 0 0 5.5C0 9.5 5.5 14 5.5 14S11 9.5 11 5.5A5.5 5.5 0 0 0 5.5 0Z" fill="#f0b429"/><circle cx="5.5" cy="5.5" r="2" fill="#fff"/></svg>
      Lumen Bildungsforum e.V<br>Ahornweg 12 – 58600 Bergfeld<br>Telefon (0 26 00) 318 42 70<br>Telefax (0 26 00) 318 42 71
    </div>
    <div class="address" style="top:210px">
      <svg width="11" height="14" viewBox="0 0 11 14" aria-hidden="true"><path d="M5.5 0A5.5 5.5 0 0 0 0 5.5C0 9.5 5.5 14 5.5 14S11 9.5 11 5.5A5.5 5.5 0 0 0 5.5 0Z" fill="#f0b429"/><circle cx="5.5" cy="5.5" r="2" fill="#fff"/></svg>
      Lumen Bildungsforum e.V<br>Mühlenstraße 21 – 58000 Talheim<br>Telefon (0 28 00) 507 93 14<br>Telefax (0 28 00) 507 93 15
    </div>
    <div class="map" role="img" aria-label="Karte des Bundeslandes mit drei Standortmarkierungen"></div>
    <div class="badges">
      <div class="badge"></div>
      <div class="badge badge--round"></div>
      <div class="badge"></div>
    </div>
  </article>

  <article class="panel panel--cover">
    <h1 class="heading cover-title">Ambulante<br>Erziehungshilfe</h1>
    <div class="photo" role="img" aria-label="Foto: aufgebrachter Vater, besorgte Mutter und genervter Jugendlicher am Tisch"
         style="left:70px;top:95px;width:297px;height:210px;background:linear-gradient(150deg,#e8eef3 0%,#b9a593 45%,#6a7da0 100%);border-radius:170px 0 0 0"></div>
    <svg class="deco" width="367" height="470" viewBox="0 0 367 470" aria-hidden="true">
      <path d="M150 40 Q50 110 80 300" fill="none" stroke="var(--blue)" stroke-width="8"/>
    </svg>
    <div class="brand"><span class="brand-mark"></span>lumen</div>
    <p class="tagline"><span class="ar">الإشراف التربوي</span>egitim yardimi<br>aide a education</p>
  </article>
</section>

</body>
</html>
```